Wine label Design

We are looking to develop an elegant contemporary Chilean design; for a new Wine Brand ZORIVEN to be sold in Chinese Market.
We would like to see designs that are a fine balance between having a traditional design that can offer quality reassurance and being distinctive enough to stand out on crowded shelves. The final design should be easy-to-remember and communicate Quality, Tradition and have a conection with Chile.

Target Market(s)

Urban Chinese between 25 to 40 yo

Requirements
Must have
• Paper label
Information on Front label : Grape (example Cabernet sauvignon) / Vintage (ex 2010) / Wine of Chile
Bottle shape is given (see attached)
Nice to have
• An element of uniqueness, easy to recall the brand
Red and Gold Color are appreciated by the Target
Should not have
• White background
Number 4 is considered death, should not be included on the design

```html
<!DOCTYPE html>
<html lang="en">
<head>
<meta charset="utf-8">
<title>ZORIVEN Wine Label</title>
<link rel="stylesheet" href="https://fonts.googleapis.com/css2?family=Poiret+One&family=Josefin+Sans:wght@300;400&family=Italianno&display=swap">
<style>
  :root {
    --backdrop: #2b2b2b;
    --label-red: #d8482c;
    --label-red-deep: #c93d24;
    --parchment-light: #f4cd82;
    --parchment: #ecbc68;
    --gold: #e2b23c;
    --gold-light: #f6d873;
    --wine-ink: #a8342c;
  }
  * { margin: 0; padding: 0; box-sizing: border-box; }
  html, body {
    width: 1004px;
    height: 1200px;
    overflow: hidden;
    background: var(--backdrop);
  }
  .canvas {
    position: relative;
    width: 1004px;
    height: 1200px;
    display: flex;
    align-items: center;
    justify-content: center;
  }
  .label {
    position: relative;
    width: 900px;
    height: 464px;
    background: radial-gradient(ellipse at 50% 45%, var(--label-red) 0%, var(--label-red-deep) 100%);
  }
  .label__rule {
    position: absolute;
    left: 0;
    right: 0;
    height: 5px;
    background: linear-gradient(90deg, var(--gold), var(--gold-light), var(--gold));
  }
  .label__rule--top { top: 4px; }
  .label__rule--bottom { bottom: 4px; }
  .label__panel {
    position: absolute;
    left: 145px;
    right: 145px;
    top: 71px;
    bottom: 71px;
    background: radial-gradient(ellipse at 50% 40%, var(--parchment-light) 0%, var(--parchment) 100%);
    display: flex;
    flex-direction: column;
    align-items: center;
    padding-top: 56px;
  }
  .label__panel::before,
  .label__panel::after {
    content: "";
    position: absolute;
    left: 0;
    right: 0;
    height: 7px;
    background: linear-gradient(90deg, var(--gold), var(--gold-light), var(--gold));
  }
  .label__panel::before { top: 0; }
  .label__panel::after { bottom: 0; }
  .brand {
    font-family: "Poiret One", sans-serif;
    font-size: 74px;
    letter-spacing: 6px;
    color: var(--wine-ink);
    line-height: 1;
  }
  .vintage {
    margin-top: 34px;
    font-family: "Josefin Sans", sans-serif;
    font-weight: 300;
    font-size: 22px;
    letter-spacing: 1px;
    color: var(--wine-ink);
  }
  .divider {
    width: 175px;
    height: 2px;
    margin: 8px 0 10px;
    background: var(--gold);
  }
  .origin {
    font-family: "Josefin Sans", sans-serif;
    font-weight: 400;
    font-size: 20px;
    color: var(--wine-ink);
  }
  .grape {
    margin-top: 26px;
    font-family: "Italianno", cursive;
    font-size: 44px;
    color: var(--wine-ink);
    line-height: 1;
  }
</style>
</head>
<body>
  <main class="canvas">
    <section class="label">
      <div class="label__rule label__rule--top"></div>
      <div class="label__panel">
        <h1 class="brand">ZORIVEN</h1>
        <p class="vintage">VINTAGE 2010</p>
        <div class="divider"></div>
        <p class="origin">WINE OF CHILE</p>
        <p class="grape">Cabernet Sauvignon</p>
      </div>
      <div class="label__rule label__rule--bottom"></div>
    </section>
  </main>
</body>
</html>
```